logo design and sales page for dodecahedrons

We sell dodecahedrons for meditation purpose. These are copper objects where you sit in (may sound strange for some of you, but it gives you a great effect).
We have a template for wordpress installed on our webserver (see https://lumoravin.at/) where we like the basic design (colour scheme) and functionality.
So we would need a Logo that is mainly comprising a dodecahedron, and if a sample picture can be made, it would be great to have a person sitting in a dodecahedron whereas the enery is visualized (see sample stock pictures).
Please check: C60_-_4_1630513838 to see the specifications of the dodecahedron.

Target Market(s)

People familiar with meditation practice, looking for inner peace and spiritual connection

Industry/Entity Type

Meditation, Yoga, Energy work, spiritual

Font styles to use
Sans Serif

Colors
F0912C
F2A743
F7CA91
FBE8D2
FDF5EE

Requirements
Must have
• The dodecahedron as a logo
Nice to have
• A person meditationg in a dodecahedron whereas the enery is visualized (see sample stock pictures)

```html
<!DOCTYPE html>
<html lang="en">
<head>
<meta charset="utf-8">
<title>Lumoravin – Meditation Dodecahedrons</title>
<link rel="stylesheet" href="https://fonts.googleapis.com/css2?family=Raleway:wght@500;600;700;800&family=Open+Sans:ital,wght@0,400;0,600;1,400&display=swap">
<style>
:root{
  --orange:#eb8125;
  --orange-soft:#f0912c;
  --ink:#1d1d1d;
  --text:#333;
  --muted:#4a4a4a;
  --paper:#f4f4f4;
  --white:#fff;
  --night:#0c0b12;
  --hero-deep:#090a3a;
  --hero-glow:#2233a8;
}
*{margin:0;padding:0;box-sizing:border-box}
html,body{width:1200px;height:3277px;overflow:hidden}
body{position:relative;font-family:"Open Sans",Arial,sans-serif;color:var(--text);background:var(--white)}
.abs{position:absolute}
.heading{font-family:"Raleway",Arial,sans-serif;font-weight:700}
.section-title{position:absolute;left:0;width:1200px;text-align:center;font-family:"Raleway",Arial,sans-serif;font-weight:700;font-size:34px;color:var(--ink);letter-spacing:-.3px}
.section-title span{color:var(--orange)}
.rule{position:absolute;left:581px;width:38px;height:4px;background:var(--orange)}

/* hero */
.hero{left:0;top:0;width:1200px;height:600px;background:radial-gradient(ellipse 260px 300px at 600px 300px,#3a4fc8 0%,var(--hero-glow) 35%,var(--hero-deep) 100%)}
.brand{font-family:"Raleway",Arial,sans-serif;font-weight:700;color:var(--white);display:flex;align-items:center;gap:10px}
.brand-mark{width:38px;height:38px;border:2px solid var(--white);border-radius:50%}
.nav{top:40px;font-family:"Raleway",Arial,sans-serif;font-weight:700;font-size:14px;color:var(--white)}
.hero-title{top:180px;left:0;width:1200px;text-align:center;font-family:"Raleway",Arial,sans-serif;font-weight:800;font-size:76px;color:var(--white);letter-spacing:-1px}
.hero-copy{top:279px;left:210px;width:780px;text-align:center;font-size:14.5px;line-height:28px;color:var(--white)}
.btn{display:flex;align-items:center;justify-content:center;border-radius:26px;font-family:"Raleway",Arial,sans-serif;font-weight:700;font-size:15px}
.btn-hero{left:499px;top:347px;width:202px;height:49px;background:var(--orange);color:var(--white)}
.dots{top:556px;left:568px;display:flex;gap:4px}
.dots i{width:9px;height:9px;border-radius:50%;background:var(--white)}
.dots i:first-child{background:var(--orange)}

/* why */
.why{left:0;top:600px;width:1200px;height:603px;background:var(--paper)}
.feature{width:240px}
.feature h3{font-family:"Raleway",Arial,sans-serif;font-weight:700;font-size:15px;color:var(--orange);margin-bottom:4px}
.feature p{font-size:13px;line-height:25px;color:var(--muted)}
.feature.left{text-align:right}
.hex{width:70px;height:62px}
.hex svg{width:70px;height:62px}
.hex b{position:absolute;inset:0;display:flex;align-items:center;justify-content:center;font-family:"Raleway",Arial,sans-serif;font-weight:700;font-size:32px;color:var(--white)}
.figure-slot{left:439px;top:783px;width:318px;height:337px;border-radius:50%;background:radial-gradient(circle,#e6e6e6 0%,var(--paper) 70%)}

/* about */
.about-photo{left:0;top:1203px;width:600px;height:593px;background:linear-gradient(135deg,#6d5d4c 0%,#a89986 45%,#584a3e 100%)}
.about-panel{left:600px;top:1203px;width:600px;height:593px;background:var(--orange)}
.about-title{left:649px;top:1275px;font-size:34px;color:var(--white)}
.about-rule{left:649px;top:1326px;width:38px;height:4px;background:var(--white)}
.about-copy{left:649px;top:1342px;width:460px;font-size:13.2px;line-height:28px;color:var(--white)}
.btn-about{left:649px;top:1663px;width:204px;height:49px;background:var(--white);color:var(--orange)}

/* testimonials */
.testi-intro{left:200px;top:1952px;width:800px;text-align:center;font-size:14px;line-height:28px;color:var(--muted)}
.avatar{width:182px;height:182px;border-radius:50%}
.quote{width:295px;font-style:italic;font-size:13px;line-height:24px;color:var(--muted)}
.person{font-family:"Raleway",Arial,sans-serif;font-weight:600;font-size:21px;color:var(--orange)}
.stars{display:flex;gap:3px}
.stars svg{width:13px;height:13px}

/* blog */
.blog{left:0;top:2301px;width:1200px;height:636px;background:var(--paper)}
.card{top:2457px;width:293px;height:406px;background:var(--white)}
.card-img{width:293px;height:209px}
.card-body{padding:14px 15px 0}
.card h4{font-family:"Raleway",Arial,sans-serif;font-weight:700;font-size:13.5px;line-height:28px;color:var(--ink)}
.card p{font-size:13.5px;line-height:28px;color:var(--muted);margin-top:2px}
.card a{font-family:"Raleway",Arial,sans-serif;font-weight:600;font-size:14px;color:var(--orange);line-height:28px}

/* footer */
.footer{left:0;top:2937px;width:1200px;height:340px;background:radial-gradient(ellipse 420px 260px at 600px 170px,#2a2238 0%,var(--night) 100%)}
.foot-h{top:3016px;font-family:"Raleway",Arial,sans-serif;font-weight:700;font-size:17px;color:var(--white)}
.foot-list{top:3050px;list-style:none;font-size:12.5px;line-height:28px;color:var(--white)}
.contact{left:515px;top:3068px;width:280px;font-size:12.5px;color:var(--white)}
.contact li{list-style:none;display:flex;gap:14px;align-items:flex-start;margin-bottom:18px;line-height:22px}
.contact svg{flex:0 0 26px;width:26px;height:26px}
.social{top:3124px;left:874px;display:flex;gap:11px}
.social span{width:34px;height:34px;border:2px solid var(--white);border-radius:50%}
.copy{top:3216px;left:0;width:1200px;text-align:center;font-size:13px;color:var(--white)}
</style>
</head>
<body>

<!-- hero -->
<section class="abs hero" role="img" aria-label="Photo of a meditating figure made of glowing blue code"></section>
<div class="abs brand" style="left:132px;top:32px;font-size:25px"><span class="brand-mark"></span>LUMORAVIN</div>
<nav>
  <span class="abs nav" style="left:547px">HOME</span>
  <span class="abs nav" style="left:623px">ABOUT</span>
  <span class="abs nav" style="left:705px">WHY CHOOSE US</span>
  <span class="abs nav" style="left:855px">TESTIMONIAL</span>
  <span class="abs nav" style="left:981px">CONTACT US</span>
</nav>
<h1 class="abs hero-title">LUMORAVIN</h1>
<p class="abs hero-copy">Lorem ipsum dolor sit amet, consectetur adipiscing elit, sed do eiusmod tempor incididunt ut labore et dolore magna aliqua. Quis ipsum suspendisse ultrices gravida. Risus commodo viverra.</p>
<a class="abs btn btn-hero">GET STARTED</a>
<div class="abs dots"><i></i><i></i><i></i><i></i><i></i></div>

<!-- why choose us -->
<section class="abs why"></section>
<h2 class="section-title" style="top:670px"><span>WHY</span> CHOOSE US</h2>
<div class="rule" style="top:722px"></div>
<div class="abs figure-slot" role="img" aria-label="Wireframe drawing of a dodecahedron"></div>

<div class="abs feature left" style="left:91px;top:760px"><h3>LOREM IPSUM DOLOR SIT</h3><p>Lorem ipsum dolor sit amet, conse ctetur adipiscing elit, sed do eiusmod tempor incididunt ut.</p></div>
<div class="abs feature left" style="left:91px;top:884px"><h3>LOREM IPSUM DOLOR SIT</h3><p>Lorem ipsum dolor sit amet, conse ctetur adipiscing elit, sed do eiusmod tempor incididunt ut.</p></div>
<div class="abs feature left" style="left:91px;top:1008px"><h3>LOREM IPSUM DOLOR SIT</h3><p>Lorem ipsum dolor sit amet, conse ctetur adipiscing elit, sed do eiusmod tempor incididunt ut.</p></div>
<div class="abs feature" style="left:868px;top:760px"><h3>LOREM IPSUM DOLOR SIT</h3><p>Lorem ipsum dolor sit amet, conse ctetur adipiscing elit, sed do eiusmod tempor incididunt ut.</p></div>
<div class="abs feature" style="left:868px;top:884px"><h3>LOREM IPSUM DOLOR SIT</h3><p>Lorem ipsum dolor sit amet, conse ctetur adipiscing elit, sed do eiusmod tempor incididunt ut.</p></div>
<div class="abs feature" style="left:868px;top:1008px"><h3>LOREM IPSUM DOLOR SIT</h3><p>Lorem ipsum dolor sit amet, conse ctetur adipiscing elit, sed do eiusmod tempor incididunt ut.</p></div>

<div class="abs hex" style="left:344px;top:765px"><svg viewBox="0 0 70 62"><polygon points="17,0 53,0 70,31 53,62 17,62 0,31" fill="#eb8125"/></svg><b>1</b></div>
<div class="abs hex" style="left:344px;top:889px"><svg viewBox="0 0 70 62"><polygon points="17,0 53,0 70,31 53,62 17,62 0,31" fill="#eb8125"/></svg><b>2</b></div>
<div class="abs hex" style="left:344px;top:1014px"><svg viewBox="0 0 70 62"><polygon points="17,0 53,0 70,31 53,62 17,62 0,31" fill="#eb8125"/></svg><b>3</b></div>
<div class="abs hex" style="left:785px;top:767px"><svg viewBox="0 0 70 62"><polygon points="17,0 53,0 70,31 53,62 17,62 0,31" fill="#eb8125"/></svg><b>4</b></div>
<div class="abs hex" style="left:785px;top:892px"><svg viewBox="0 0 70 62"><polygon points="17,0 53,0 70,31 53,62 17,62 0,31" fill="#eb8125"/></svg><b>5</b></div>
<div class="abs hex" style="left:785px;top:1010px"><svg viewBox="0 0 70 62"><polygon points="17,0 53,0 70,31 53,62 17,62 0,31" fill="#eb8125"/></svg><b>6</b></div>

<!-- about -->
<div class="abs about-photo" role="img" aria-label="Photo of a copper dodecahedron frame around an armchair in a living room"></div>
<section class="abs about-panel"></section>
<h2 class="abs heading about-title">ABOUT&nbsp; LUMORAVIN</h2>
<div class="abs about-rule"></div>
<p class="abs about-copy">Lorem ipsum dolor sit amet, consectetur adipiscing elit, sed do eiusmod tempor incididunt ut labore et dolore magna aliqua. Ut enim ad minim veniam, quis nostrud exercitation ullamco laboris nisi ut aliquip ex ea commodo consequat. Duis aute irure dolor in reprehenderit in voluptate velit esse cillum dolore eu fugiat nulla pariatur. Excepteur sint occaecat cupidatat non proident, sunt in culpa qui officia deserunt mollit anim id est laborum.Sed ut perspiciatis unde omnis iste natus error sit voluptatem accusantium doloremque laudantium, totam rem aperiam, eaque ipsa quae ab illo inventore veritatis et quasi architecto beatae vitae dicta sunt explicabo. Nemo enim ipsam voluptatem quia voluptas sit aspernatur aut odit aut fugit sed quia consequuntur.</p>
<a class="abs btn btn-about">LEARN MORE</a>

<!-- testimonials -->
<h2 class="section-title" style="top:1866px"><span>OUR</span> CLIENT TESTIMONIALS</h2>
<div class="rule" style="top:1917px"></div>
<p class="abs testi-intro">Lorem ipsum dolor sit amet, consectetur adipiscing elit, sed do eiusmod tempor incididunt ut labore et dolore magna aliqua. Ut enim ad minim veniam, quis nostrud exercitation ullamco laboris nisi ut aliquip.</p>

<div class="abs avatar" style="left:74px;top:2034px;background:radial-gradient(circle at 50% 45%,#c98e74 0%,#7a3b2a 60%,#b3232a 100%)" role="img" aria-label="Portrait photo of a smiling woman"></div>
<p class="abs quote" style="left:276px;top:2034px">Lorem ipsum dolor sit amet, consectetur adipiscing elit, sed do eiusmod tempor incididunt ut labore et dolore magna aliqua. Ut enim ad minim veniam, quis nostrud exercitation ullamco laboris nisi ut aliquip ex ea.</p>
<div class="abs person" style="left:276px;top:2185px">John Deo</div>
<div class="abs stars" style="left:483px;top:2195px"><svg viewBox="0 0 24 24"><polygon points="12,1 15,9 23,9 17,14 19,23 12,18 5,23 7,14 1,9 9,9" fill="#f0912c"/></svg><svg viewBox="0 0 24 24"><polygon points="12,1 15,9 23,9 17,14 19,23 12,18 5,23 7,14 1,9 9,9" fill="#f0912c"/></svg><svg viewBox="0 0 24 24"><polygon points="12,1 15,9 23,9 17,14 19,23 12,18 5,23 7,14 1,9 9,9" fill="#f0912c"/></svg><svg viewBox="0 0 24 24"><polygon points="12,1 15,9 23,9 17,14 19,23 12,18 5,23 7,14 1,9 9,9" fill="#f0912c"/></svg><svg viewBox="0 0 24 24"><polygon points="12,1 15,9 23,9 17,14 19,23 12,18 5,23 7,14 1,9 9,9" fill="#f0912c"/></svg></div>

<p class="abs quote" style="left:632px;top:2034px">Lorem ipsum dolor sit amet, consectetur adipiscing elit, sed do eiusmod tempor incididunt ut labore et dolore magna aliqua. Ut enim ad minim veniam, quis nostrud exercitation ullamco laboris nisi ut aliquip ex ea.</p>
<div class="abs person" style="left:632px;top:2185px">John Deo</div>
<div class="abs stars" style="left:840px;top:2195px"><svg viewBox="0 0 24 24"><polygon points="12,1 15,9 23,9 17,14 19,23 12,18 5,23 7,14 1,9 9,9" fill="#f0912c"/></svg><svg viewBox="0 0 24 24"><polygon points="12,1 15,9 23,9 17,14 19,23 12,18 5,23 7,14 1,9 9,9" fill="#f0912c"/></svg><svg viewBox="0 0 24 24"><polygon points="12,1 15,9 23,9 17,14 19,23 12,18 5,23 7,14 1,9 9,9" fill="#f0912c"/></svg><svg viewBox="0 0 24 24"><polygon points="12,1 15,9 23,9 17,14 19,23 12,18 5,23 7,14 1,9 9,9" fill="#f0912c"/></svg><svg viewBox="0 0 24 24"><polygon points="12,1 15,9 23,9 17,14 19,23 12,18 5,23 7,14 1,9 9,9" fill="#f0912c"/></svg></div>
<div class="abs avatar" style="left:944px;top:2034px;background:radial-gradient(circle at 50% 40%,#c99a7e 0%,#6e6a64 55%,#2fa6c8 100%)" role="img" aria-label="Portrait photo of a smiling man"></div>

<!-- blog -->
<section class="abs blog"></section>
<h2 class="section-title" style="top:2370px"><span>OUR</span> LATEST BLOG</h2>
<div class="rule" style="top:2421px"></div>

<article class="abs card" style="left:135px">
  <div class="card-img" style="background:radial-gradient(circle at 55% 50%,#b9893a 0%,#4a4236 50%,#2a2f3d 100%)" role="img" aria-label="Glowing golden dodecahedron in a dark room"></div>
  <div class="card-body"><h4>LOREM IPSUM DOLOR SIT AMET CO TUR ADIPISCING ELIT SED DO</h4><p>Lorem ipsum dolor sit amet, consectetur adipiscing elit, sed do eiusmod tempor indidunt ut labore et dolore magna.</p><a>LEARN MORE</a></div>
</article>
<article class="abs card" style="left:454px">
  <div class="card-img" style="background:radial-gradient(circle at 50% 55%,#3fa9d6 0%,#6a2a8a 40%,#07081a 85%)" role="img" aria-label="Colourful illustration of a meditating figure"></div>
  <div class="card-body"><h4>LOREM IPSUM DOLOR SIT AMET CO TUR ADIPISCING ELIT SED DO</h4><p>Lorem ipsum dolor sit amet, consectetur adipiscing elit, sed do eiusmod tempor indidunt ut labore et dolore magna.</p><a>LEARN MORE</a></div>
</article>
<article class="abs card" style="left:774px">
  <div class="card-img" style="background:radial-gradient(ellipse at 50% 40%,#b13a9a 0%,#3b2f7a 45%,#1a2a3a 100%)" role="img" aria-label="Meditating figure surrounded by swirling energy light"></div>
  <div class="card-body"><h4>LOREM IPSUM DOLOR SIT AMET CO TUR ADIPISCING ELIT SED DO</h4><p>Lorem ipsum dolor sit amet, consectetur adipiscing elit, sed do eiusmod tempor indidunt ut labore et dolore magna.</p><a>LEARN MORE</a></div>
</article>

<!-- footer -->
<footer class="abs footer" role="img" aria-label="Dark background with a faint glowing meditation scene"></footer>
<h5 class="abs foot-h" style="left:120px">QUICK LINKS</h5>
<ul class="abs foot-list" style="left:121px"><li>Home</li><li>About</li><li>Why Choose Us</li><li>Testimonial</li><li>Contact Us</li></ul>
<h5 class="abs foot-h" style="left:322px">LEGAL</h5>
<ul class="abs foot-list" style="left:321px"><li>Terms &amp; Conditions</li><li>privacy Policy</li><li>FAQ</li><li>Sitmap</li></ul>
<h5 class="abs foot-h" style="left:516px">CONTACT US</h5>
<ul class="abs contact">
  <li><svg viewBox="0 0 26 26"><circle cx="13" cy="13" r="13" fill="#eb8125"/><path d="M13 6a5 5 0 0 0-5 5c0 4 5 9 5 9s5-5 5-9a5 5 0 0 0-5-5z" fill="#fff"/><circle cx="13" cy="11" r="2" fill="#eb8125"/></svg><span>123 Sed ut perspiciatis unde omnis is te natus error sit voluptatem</span></li>
  <li><svg viewBox="0 0 26 26"><circle cx="13" cy="13" r="13" fill="#eb8125"/><rect x="7" y="9" width="12" height="8" fill="#fff"/><path d="M7 9l6 5 6-5" fill="none" stroke="#eb8125" stroke-width="1.2"/></svg><span>info@lumoravin.at</span></li>
  <li><svg viewBox="0 0 26 26"><circle cx="13" cy="13" r="13" fill="#eb8125"/><path d="M9 7l3 3-2 2c1 2 2 3 4 4l2-2 3 3-2 2c-5 0-10-5-10-10z" fill="#fff"/></svg><span>123 456 7890</span></li>
</ul>
<div class="abs brand" style="left:840px;top:3042px;font-size:25px"><span class="brand-mark" style="width:44px;height:44px"></span>LUMORAVIN</div>
<div class="abs social"><span aria-label="Social profile"></span><span aria-label="Social profile"></span><span aria-label="Social profile"></span><span aria-label="Social profile"></span></div>
<p class="abs copy">© 2021&nbsp; Lumoravin.&nbsp; | All Rights Reserved</p>

</body>
</html>
```